4 Seitiger DIN A4 Flyer für Angebote (DIN A3 gefaltet)
Zielgruppe
Ich handel und montiere z.B. Hochwertige Fenster, Türen und Parkett.
Zielgruppen sind: Architekten, Baufirmen, Hausbauer sowie Hausbesitzer und Sanierer
Aufgabenstellung
Die Farben aus meinem Logo: Grün, Antrazith, Schwarz.
Der 4 Seitige Flyer soll als Aktionsflyer in der Tageszeitung verteilt werden.
Im Innenteil des Flyers sollten Die Parkettböden und 2 Zimmertüren angeboten werden.
Die Texte :
zu den jeweiligen Bildern gehört der qm Preis und der Satz: "zb. Landhausdiele Eiche, geölt Format 2200x180mm, Nutzschicht 2,5mm"
Ansonsten weis ich nicht was noch textlich verkaufsfördernd wäre
Die Rückseite mit Anschrift, Aktions-Treppen Sanierung oder Neubau( ab 1450.- ), Außenverschalung.

```html
<!DOCTYPE html>
<html lang="de">
<head>
<meta charset="utf-8">
<title>Brandt – Aktionsflyer Parkett &amp; Innentüren</title>
<link href="https://fonts.googleapis.com/css2?family=Jost:wght@400;500;600&family=Mulish:wght@400;600;700&display=swap" rel="stylesheet">
<style>
:root{
  --green:#97c33d;
  --ink:#1f1f1f;
  --text:#333333;
  --stage:#8f8f8f;
  --paper:#ffffff;
  --oak-mid:#b8875a;
}
*{box-sizing:border-box;margin:0;padding:0}
html,body{width:1200px;height:2400px;overflow:hidden;background:var(--stage)}
body{position:relative;font-family:"Mulish",sans-serif;color:var(--text)}
.page{position:absolute;background:var(--paper);overflow:hidden;box-shadow:2px 3px 6px rgba(0,0,0,.25)}
.brand{position:absolute;display:flex;align-items:center;gap:6px}
.brand-name{font-family:"Jost",sans-serif;font-weight:600;color:var(--ink);letter-spacing:-1px;line-height:1}
.brand-mark{background:var(--green)}
.photo{position:absolute}
.wood-floor{background:linear-gradient(160deg,#e8e4de 0%,#cdb493 35%,var(--oak-mid) 70%,#a8754a 100%)}

/* cover */
.cover{left:590px;top:75px;width:507px;height:717px}
.cover .brand{right:32px;top:25px}
.cover .brand-name{font-size:58px}
.cover .brand-mark{width:84px;height:84px}
.cover-photo{left:0;top:140px;width:507px;height:577px}
.cover-thumbs{position:absolute;left:0;top:537px;width:258px;height:129px;background:var(--paper);padding:3px 4px 3px 0;display:flex;gap:4px}
.cover-thumbs div{flex:1}
.thumb-floor{background:linear-gradient(135deg,#eae6e0,#c9a57c)}
.thumb-door{background:linear-gradient(90deg,#f3f2f0 0%,#f3f2f0 40%,#c49a68 55%,#c49a68 75%,#f1efec 100%)}
.cover-title{position:absolute;left:269px;top:548px;font-family:"Jost",sans-serif;color:#fff;font-weight:500;line-height:1.15;text-transform:uppercase}
.cover-title .line{font-size:27px;display:block}
.cover-title .big{font-size:52px;font-weight:600;line-height:1.05}
.issue-tab{position:absolute;left:475px;top:537px;width:32px;height:132px;background:var(--green);display:flex;align-items:center;justify-content:center}
.issue-tab span{transform:rotate(-90deg);font-size:13px;color:var(--ink);white-space:nowrap}
.cover-url{position:absolute;left:0;width:507px;top:690px;text-align:center;color:#fff;font-weight:600;font-size:13px;padding-left:30px}

/* spread */
.spread-left{left:84px;top:834px;width:507px;height:716px}
.spread-right{left:591px;top:834px;width:506px;height:716px}
.spread-head{position:absolute;left:0;top:0;width:100%;height:149px}
.spread-right .spread-head{background:var(--green)}
.spread-head .brand{left:53px;top:34px}
.spread-head .brand-name{font-size:40px}
.spread-head .brand-mark{width:56px;height:56px}
.spread-right .brand-mark{background:#fff}
.section-title{position:absolute;left:250px;top:34px;font-family:"Jost",sans-serif;font-size:13.5px;font-weight:500;color:var(--green);letter-spacing:.2px}
.spread-right .section-title{color:#fff}
.intro{position:absolute;left:250px;top:58px;width:200px;font-size:9px;line-height:1.25;color:var(--text)}
.spread-right .intro{color:#fff}
.intro .drop{float:left;font-family:"Jost",sans-serif;font-size:25px;line-height:.85;margin-right:2px}

.floor-grid{position:absolute;left:0;top:149px;width:507px;display:grid;grid-template-columns:250px 252px;column-gap:5px}
.floor-item{position:relative;height:188px}
.floor-item .photo{left:0;top:0;width:100%;height:125px}
.floor-name{position:absolute;left:33px;top:135px;font-size:9px;font-weight:700;color:var(--ink);text-transform:uppercase}
.floor-item:nth-child(even) .floor-name{left:22px}
.floor-spec{position:absolute;left:33px;top:148px;font-size:7.5px;line-height:1.3;color:var(--text)}
.floor-item:nth-child(even) .floor-spec{left:22px}
.price{position:absolute;background:var(--green);border:3px solid #fff;color:#fff;text-align:center}
.price .unit{display:block;font-size:9.5px;margin-top:6px;color:var(--ink)}
.price .amount{display:block;font-size:22px;font-weight:700;font-style:italic;line-height:1.1}
.price sup{font-size:12px}
.floor-item .price{left:164px;top:102px;width:64px;height:62px}
.floor-item:nth-child(even) .price{left:160px}
.wood-a{background:linear-gradient(180deg,#c49a6c,#a97d52)}
.wood-b{background:linear-gradient(180deg,#8a6141,#6e4b30)}
.wood-c{background:linear-gradient(180deg,#c8a88a,#b29275)}
.wood-d{background:linear-gradient(180deg,#9c7a55,#b8956c)}
.wood-e{background:linear-gradient(180deg,#6d4e36,#8d6a4c)}
.wood-f{background:linear-gradient(180deg,#c39465,#a87a4f)}

.door{position:absolute;top:189px;height:386px}
.door-white{left:51px;width:182px;background:linear-gradient(90deg,#f4f4f4,#e9e9e9)}
.door-oak{left:277px;width:180px;background:linear-gradient(90deg,#c8a06c,#b88c59)}
.door-item .price{top:545px;width:62px;height:62px}
.door-item .price .amount{font-size:19px}
.door-name{position:absolute;top:614px;font-size:9px;font-weight:700;color:var(--ink);text-transform:uppercase}
.door-desc{position:absolute;top:632px;width:182px;font-size:7.3px;line-height:1.3;color:var(--text)}

/* back */
.back{left:84px;top:1598px;width:507px;height:716px}
.back .brand{right:31px;top:25px}
.back .brand-name{font-size:58px}
.back .brand-mark{width:84px;height:84px}
.cladding-photo{left:0;top:137px;width:507px;height:268px;background:linear-gradient(110deg,#d9dde2 0%,#7d5a3c 22%,#9a7251 50%,#2a2826 62%,#6b4c33 80%,#b8b2a8 100%)}
.cladding-text{position:absolute;left:35px;top:245px;color:#fff;font-family:"Jost",sans-serif;font-size:22px;line-height:1.15}
.cladding-text strong{font-weight:500;display:block}
.cladding-text span{font-weight:400;display:block;font-size:19px}
.stairs-a{left:0;top:410px;width:157px;height:214px;background:linear-gradient(160deg,#f1efec 0%,#d9c3a6 55%,#b07d4e 100%)}
.stairs-b{left:163px;top:410px;width:150px;height:214px;background:linear-gradient(170deg,#f3f2f0 0%,#c8965f 60%,#a06a3d 100%)}
.stairs-offer{position:absolute;left:318px;top:410px;width:189px;height:214px;background:var(--green);padding:46px 0 0 33px;font-family:"Jost",sans-serif;color:var(--ink);line-height:1.1}
.stairs-offer .l{display:block;font-size:19px;font-weight:500}
.stairs-offer .xl{display:block;font-size:23px;font-weight:600}
.stairs-offer .from{display:block;margin-top:16px;font-size:19px;color:#fff;font-weight:500}
.stairs-offer .from em{font-style:italic}
.contact{position:absolute;left:0;width:507px;top:650px;text-align:center;font-size:10px;line-height:1.6;color:var(--ink);font-style:normal}
.contact .url{display:block;font-weight:700;font-size:12px;margin-top:3px}
</style>
</head>
<body>

<section class="page cover">
  <div class="brand"><span class="brand-name">Brandt</span><span class="brand-mark"></span></div>
  <div class="photo wood-floor cover-photo" role="img" aria-label="Foto: heller Eichenparkett im Fischgrätmuster in einem Flur"></div>
  <div class="cover-thumbs">
    <div class="thumb-floor" role="img" aria-label="Foto: Parkettboden mit weißer Tür"></div>
    <div class="thumb-door" role="img" aria-label="Foto: geöffnete Innentür in Eichenoptik"></div>
  </div>
  <h1 class="cover-title"><span class="line">Parketböden</span><span class="line">&amp; Innentüren</span><span class="line big">Aktion</span></h1>
  <div class="issue-tab"><span>06/2017</span></div>
  <p class="cover-url">www.brandt-schreinerei.de</p>
</section>

<section class="page spread-left">
  <header class="spread-head">
    <div class="brand"><span class="brand-name">Brandt</span><span class="brand-mark"></span></div>
    <h2 class="section-title">PARKETBÖDEN</h2>
    <p class="intro"><span class="drop">Q</span>ualität, die man spürt: Unsere geölten Landhausdielen verbinden natürliche Holzoptik mit langer Haltbarkeit. Jetzt zu Aktionspreisen inklusive Beratung, Lieferung und auf Wunsch Verlegung durch unser Team.</p>
  </header>
  <div class="floor-grid">
    <article class="floor-item">
      <div class="photo wood-a" role="img" aria-label="Holzmuster Feldberg"></div>
      <h3 class="floor-name">Feldberg</h3>
      <p class="floor-spec">Landhausdiele, geölt<br>2200x180mm, Nutzschicht 2,5mm</p>
      <div class="price"><span class="unit">€/m²</span><span class="amount">00,<sup>00</sup></span></div>
    </article>
    <article class="floor-item">
      <div class="photo wood-b" role="img" aria-label="Holzmuster Karamelleiche"></div>
      <h3 class="floor-name">Karamelleiche</h3>
      <p class="floor-spec">Landhausdiele Karamelleiche, geölt<br>2200x180mm, Nutzschicht 2,5mm</p>
      <div class="price"><span class="unit">€/m²</span><span class="amount">00,<sup>00</sup></span></div>
    </article>
    <article class="floor-item">
      <div class="photo wood-c" role="img" aria-label="Holzmuster Saphira"></div>
      <h3 class="floor-name">Saphira</h3>
      <p class="floor-spec">Landhausdiele, geölt<br>2200x180mm, Nutzschicht 2,5mm</p>
      <div class="price"><span class="unit">€/m²</span><span class="amount">00,<sup>00</sup></span></div>
    </article>
    <article class="floor-item">
      <div class="photo wood-d" role="img" aria-label="Holzmuster Nordland"></div>
      <h3 class="floor-name">Nordland</h3>
      <p class="floor-spec">Landhausdiele, geölt<br>2200x180mm, Nutzschicht 2,5mm</p>
      <div class="price"><span class="unit">€/m²</span><span class="amount">00,<sup>00</sup></span></div>
    </article>
    <article class="floor-item">
      <div class="photo wood-e" role="img" aria-label="Holzmuster Nussbaum"></div>
      <h3 class="floor-name">Nussbaum</h3>
      <p class="floor-spec">Landhausdiele Nussbaum, geölt<br>2200x180mm, Nutzschicht 2,5mm</p>
      <div class="price"><span class="unit">€/m²</span><span class="amount">00,<sup>00</sup></span></div>
    </article>
    <article class="floor-item">
      <div class="photo wood-f" role="img" aria-label="Holzmuster Wildbach"></div>
      <h3 class="floor-name">Wildbach</h3>
      <p class="floor-spec">Landhausdiele, geölt<br>2200x180mm, Nutzschicht 2,5mm</p>
      <div class="price"><span class="unit">€/m²</span><span class="amount">00,<sup>00</sup></span></div>
    </article>
  </div>
</section>

<section class="page spread-right">
  <header class="spread-head">
    <div class="brand"><span class="brand-name">Brandt</span><span class="brand-mark"></span></div>
    <h2 class="section-title">INNENTÜREN</h2>
    <p class="intro"><span class="drop">E</span>ine neue Tür verändert den ganzen Raum. Ob klassisch weiß oder in warmer Eichenoptik – wir liefern und montieren Ihre Innentüren sauber und termingerecht. Zarge, Drücker und Einbau aus einer Hand.</p>
  </header>
  <article class="door-item">
    <div class="door door-white" role="img" aria-label="Produktfoto: weiße Profiltür mit zwei Kassetten"></div>
    <div class="price" style="left:149px"><span class="unit">€/Stk.</span><span class="amount">000,-</span></div>
    <h3 class="door-name" style="left:51px">Profiltür weiss</h3>
    <p class="door-desc" style="left:51px">Zeitlose Profiltür in Weißlack mit zwei Kassetten. Komplett mit Zarge, Bändern und Buntbartschloss. Pflegeleicht, robust und passend zu jedem Einrichtungsstil. Standardmaß 860x1985mm, weitere Maße auf Anfrage.</p>
  </article>
  <article class="door-item">
    <div class="door door-oak" role="img" aria-label="Produktfoto: glatte Tür in Eichenoptik mit Quermaserung"></div>
    <div class="price" style="left:370px"><span class="unit">€/Stk.</span><span class="amount">000,-</span></div>
    <h3 class="door-name" style="left:277px">Landeiche quer</h3>
    <p class="door-desc" style="left:277px">Glatte Tür in Eiche-Dekor mit querliegender Maserung. Natürliche Optik, widerstandsfähige Oberfläche. Inklusive Zarge und Beschlag. Standardmaß 860x1985mm, Sondermaße und passende Drücker auf Anfrage.</p>
  </article>
</section>

<section class="page back">
  <div class="brand"><span class="brand-name">Brandt</span><span class="brand-mark"></span></div>
  <div class="photo cladding-photo" role="img" aria-label="Foto: Anbau mit horizontaler Holzverschalung"></div>
  <p class="cladding-text"><strong>Außenverschalung<br>aus Holz,</strong><span>die Ihnen lange<br>Freude bereiten wird.</span></p>
  <div class="photo stairs-a" role="img" aria-label="Foto: Holztreppe mit Glasgeländer und Lichtleiste"></div>
  <div class="photo stairs-b" role="img" aria-label="Foto: sanierte Treppe mit Eichenstufen"></div>
  <div class="stairs-offer">
    <span class="l">Aktions-</span>
    <span class="xl">TREPPEN</span>
    <span class="l">Sanierung</span>
    <span class="l">oder Neubau</span>
    <span class="from">ab € <em>1450.-</em></span>
  </div>
  <address class="contact">
    D-12345 Musterdorf, Am Anger 7 / beim Gutshof<br>
    T: +49 1234 567 89 00 • info@brandt-schreinerei.de
    <span class="url">www.brandt-schreinerei.de</span>
  </address>
</section>

</body>
</html>
```